Copperline Business Management Business Card Design Project

I have a new business called Copperline Business Management Limited. We provide business services for the UK for areas which include

Mentoring / Coaching
Interim Management
Non Executive Director / Chairman placement
Angel Investment support
Merger & Acquisition advice
Selling your business advice

I would like a background colour on the logo, a logo and our company name on the logo if possible.

I am open to colours but we want to portray a strong safe business with credibility

The business card design must match that of the logo design
Updates

Target Market(s)

SME and Medium size businesses with the owners, MD's, CEO or senior management as the target audiabce

Industry/Entity Type

Business

Requirements
Must have
• Match the logo design.
Look professional and quality
Should not have
• Old style text and colours
Poor logos depicting money

```html
<!DOCTYPE html>
<html lang="en">
<head>
<meta charset="utf-8">
<title>Copperline Business Management – Business Card</title>
<link rel="stylesheet" href="https://fonts.googleapis.com/css2?family=Carlito:wght@400;700&family=Cormorant+SC:wght@700&display=swap">
<style>
  :root {
    --brand-blue: #0b9bd9;
    --ink: #1a1a1a;
    --shadow-band: #0d0d0d;
    --paper: #f7f7f7;
    --backdrop: #e6e7e9;
    --white: #ffffff;
  }
  * { box-sizing: border-box; margin: 0; padding: 0; }
  html, body {
    width: 1200px; height: 1200px; overflow: hidden;
    background: var(--backdrop);
  }
  .card {
    position: absolute; left: 100px; top: 314px;
    width: 1000px; height: 571px;
    background: var(--paper);
    overflow: hidden;
    box-shadow: 0 18px 40px rgba(0,0,0,0.12);
    font-family: "Carlito", "Calibri", sans-serif;
  }
  .card__swoosh { position: absolute; left: 0; top: 0; }
  .brand {
    position: absolute; left: 560px; top: 44px;
    display: flex; align-items: center; gap: 14px;
  }
  .brand__dot {
    width: 60px; height: 60px; border-radius: 50%;
    background: var(--brand-blue); flex: none;
  }
  .brand__name {
    color: var(--brand-blue); font-weight: 700;
    font-size: 22px; line-height: 1.08;
  }
  .contact-box {
    position: absolute; left: 610px; top: 232px; z-index: 2;
    width: 390px; height: 168px;
    background: var(--brand-blue);
    color: var(--white);
    padding: 34px 0 0 22px;
    font-size: 23px; line-height: 1.3;
    white-space: nowrap;
  }
  .person {
    position: absolute; left: 252px; top: 308px;
    width: 340px;
    color: var(--brand-blue);
    white-space: nowrap;
  }
  .person__name {
    font-family: "Cormorant SC", "Palatino Linotype", serif;
    font-weight: 700; font-size: 30px; line-height: 1;
  }
  .person__role { font-size: 24px; margin-top: 12px; }
  .divider {
    position: absolute; left: 240px; top: 398px;
    width: 370px; border-top: 2px dotted var(--brand-blue);
  }
  .address {
    position: absolute; left: 252px; top: 428px;
    color: var(--ink); font-size: 24px; line-height: 1.32;
    white-space: nowrap;
  }
</style>
</head>
<body>
  <div class="card">
    <svg class="card__swoosh" width="500" height="300" viewBox="0 0 500 300" aria-hidden="true">
      <path d="M0 0 H452 C450 150 320 244 0 258 Z" fill="var(--shadow-band)"/>
      <path d="M0 0 H430 C426 140 300 228 0 240 Z" fill="var(--brand-blue)"/>
    </svg>

    <div class="brand">
      <span class="brand__dot"></span>
      <div class="brand__name">Copperline<br>Business<br>Management LTD</div>
    </div>

    <div class="contact-box">
      Phone : (01) 4270 1183<br>
      Mobile : (01) 4270 1184<br>
      Fax : (01) 4270 1185
    </div>

    <div class="person">
      <div class="person__name">Mr. Daniel Roe Hart</div>
      <div class="person__role">CEO</div>
    </div>

    <div class="divider"></div>

    <div class="address">
      Unit 8, 14 Mercer Row<br>
      Kingsbridge, KB2 7TR<br>
      www.copperlinebm.co.uk
    </div>
  </div>
</body>
</html>
```